Business Card & Logo Design - Hedge Fund

We need a business card and logo design for a hedge fund. The hedge fund is named Morvane Holdings LLC. Morvane Holdings was created by finance professors and the strategy is based academic research that looks for patterns in stock prices. The design should look conservative, solid, strong. We favor a classic style - nothing flashy. The logo can relate to the name Morvane Holdings, or it could involve a symbol design that connotes "science" . We are open to ideas. We do not want alot of colors - but if any, color - blue is preferred. The font that seems to look best for the name (Morvane Holdings) is arial black. We are open to ideas. Most important - we want to see a mock up of an actual business card with the logo concept embedded. The business card should include space for : company name, individual name, position title, cell phone, address. We hope to have this work done by Sept. 8.

Target Market(s)

We will be meeting with and giving the business card to institutions and high net worth individuals.

Industry/Entity Type

Investment Advisory

Contact Information for Business Card

Company name - Morvane Holdings LLC
Individual name - Peter Vosk
Title - Portfolio Manager
Cell - (482) 555-0137
Address - 2750 Birchwell Lane, Suite 300, Atlanta GA 30327

Font styles to use
Other font styles liked:
• Arial

Colors
3277b5
0255a3
85acd3
cedeed
fdf9cf
d9d9d9
e6e6e6
f04a50
6b449b

Requirements
Must have
• Must have card details that are sited above.
• We would like a logo related to the name (Morvane Holdings) or concept of the fund.
Nice to have
• We want conservative / understated / clean crisp look.
• If any colors - we prefer conservative appearance - blue / gray.
• I have enclosed an example of a card style that looks attractive - please do not exactly copy this card. This is not our company or logo. I feel the layout is attractive - just as an example
Should not have
• Avoid too much color.
• I have selected some preferred colors. Please do not use all of the colors - I have selected a few that might work - but I am not sure. We are open to your ideas so please do not feel the need to use all or any of these.

```html
<!DOCTYPE html>
<html lang="en">
<head>
<meta charset="utf-8">
<title>Morvane Holdings LLC – Business Card</title>
<link href="https://fonts.googleapis.com/css2?family=Archivo+Black&family=Arimo:wght@400;700&display=swap" rel="stylesheet">
<style>
  :root {
    --navy: #28256e;
    --navy-deep: #232063;
    --gray: #8a8a8a;
    --text-gray: #6f6f6f;
    --paper: #ffffff;
    --stage: #2e2e30;
  }
  * { box-sizing: border-box; margin: 0; padding: 0; }
  html, body { width: 1200px; height: 1200px; overflow: hidden; }
  body {
    background: var(--stage);
    display: flex;
    flex-direction: column;
    align-items: center;
    justify-content: center;
    gap: 40px;
  }
  .card {
    position: relative;
    width: 860px;
    height: 491px;
    overflow: hidden;
    box-shadow: 0 14px 30px rgba(0,0,0,0.45);
  }

  /* Back of card */
  .card-back { background: var(--navy); }
  .card-back__texture {
    position: absolute; inset: 0;
    background: radial-gradient(circle at 50% 45%, var(--navy) 0%, var(--navy-deep) 100%);
  }
  .card-back__brand {
    position: absolute; inset: 0;
    display: flex; flex-direction: column;
    align-items: center; justify-content: center;
    gap: 26px;
  }
  .brand-dot {
    width: 96px; height: 96px; border-radius: 50%;
    background: var(--gray);
  }
  .brand-name {
    font-family: "Archivo Black", "Arial Black", sans-serif;
    font-size: 40px;
    letter-spacing: 0.5px;
    white-space: nowrap;
  }
  .card-back .brand-name { color: #ffffff; }

  /* Front of card */
  .card-front { background: var(--paper); display: flex; align-items: center; }
  .card-front__brand {
    width: 400px;
    flex: none;
    display: flex; flex-direction: column;
    align-items: center; gap: 18px;
    padding: 0 24px 0 40px;
  }
  .card-front .brand-dot { width: 80px; height: 80px; background: var(--navy); }
  .card-front .brand-name { color: var(--navy); font-size: 24px; letter-spacing: 0.3px; }
  .card-front__divider {
    width: 2px; height: 200px; background: var(--navy); flex: none;
  }
  .card-front__details { padding-left: 52px; }
  .person-name {
    font-family: "Archivo Black", "Arial Black", sans-serif;
    color: var(--navy);
    font-size: 27px;
    line-height: 1.1;
  }
  .person-title {
    font-family: "Arimo", Arial, sans-serif;
    color: var(--text-gray);
    font-size: 17px;
    margin: 6px 0 24px;
  }
  .contact-list { list-style: none; }
  .contact-item {
    display: flex; align-items: flex-start; gap: 12px;
    font-family: "Arimo", Arial, sans-serif;
    font-size: 19px; line-height: 1.25;
    color: var(--text-gray);
    margin-bottom: 6px;
  }
  .contact-icon { width: 16px; height: 16px; flex: none; margin-top: 3px; fill: var(--navy); }
</style>
</head>
<body>

  <section class="card card-back" aria-label="Card back">
    <div class="card-back__texture" role="img" aria-label="Faint repeating pattern on navy background"></div>
    <div class="card-back__brand">
      <span class="brand-dot"></span>
      <span class="brand-name">Morvane Holdings LLC</span>
    </div>
  </section>

  <section class="card card-front" aria-label="Card front">
    <div class="card-front__brand">
      <span class="brand-dot"></span>
      <span class="brand-name">Morvane Holdings LLC</span>
    </div>
    <div class="card-front__divider"></div>
    <div class="card-front__details">
      <h1 class="person-name">Peter Vosk</h1>
      <p class="person-title">Portfolio Manager</p>
      <ul class="contact-list">
        <li class="contact-item">
          <svg class="contact-icon" viewBox="0 0 16 16" aria-hidden="true"><path d="M4 1l3 3-2 2c1 2 3 4 5 5l2-2 3 3-2 2C7 14 2 9 2 3z"/></svg>
          <span>(482) 555-0137</span>
        </li>
        <li class="contact-item">
          <svg class="contact-icon" viewBox="0 0 16 16" aria-hidden="true"><rect x="1" y="3" width="14" height="10" rx="1"/><path d="M1.5 3.5l6.5 5.5 6.5-5.5" fill="none" stroke="#fff" stroke-width="1.3"/></svg>
          <span>vosk@morvane.com</span>
        </li>
        <li class="contact-item">
          <svg class="contact-icon" viewBox="0 0 16 16" aria-hidden="true"><path d="M8 0a5 5 0 0 1 5 5c0 4-5 11-5 11S3 9 3 5a5 5 0 0 1 5-5zm0 3a2 2 0 1 0 0 4 2 2 0 0 0 0-4z"/></svg>
          <span>2750 Birchwell Lane, Suite 300<br>Atlanta, GA 30327</span>
        </li>
      </ul>
    </div>
  </section>

</body>
</html>
```